Veterinary Hospital Brochure - 2 Drafts - 1 Normal and 1 Fun.

Meadowbrook Pet Hospital needs a brochure to promote our veterinary hospital. These will be delivered to local mailboxes. I would like to see atleast 2 submissions from each designer.
One submission conservative and A4 folded DL and another submission more radical and interesting with innovative folding or crazy concepts. Maybe the brochure could be designed to fold into a dog house ?
I want at least one version to be VERY SIMPLE AND INTIMATE.
Our existing website is here: http://furlane.example/ and our new website will look like this: http://trial4.pagemint.example/#home
Please use colors and images from the new website, and information from the old website. The heading font used in the new site is Qorvatype - Otter Tilt Sketchline
I want the brochure to be simple and engaging on first view, and then provide the opportunity to find more information if desired. The brochure needs to be captivating on the outside so people don't throw it away immediately.

We will soon need letterhead, flags, pens, business cards, signs and vouchers so there is the opportunity for more work for the successful designer.

Target Market(s)

Women 25 to 44

Industry/Entity Type

Veterinary

Contact Information for Business Card

Meadowbrook Pet Hospital
14 Marlow Crescent
Tamsworth Vale
NSW 2417
Phone: 02 61938205
Emergency: 0417360592
Fax: 02 83159462
www.meadowbrookvets.example
contact@meadowbrookvets.example

Font styles to use
Script

Requirements
Must have
• Colors from the new website: http://meadowbrookvets.example/ and new logo.
• Information from the old website: http://furlane.example/
• 2 drafts - A normal A4 folded DL flyer and an interesting crazy design.
Nice to have
• VERY SIMPLE
• Subdued
• Intimate
Should not have
• Intense colours
• Red

```html
<!DOCTYPE html>
<html lang="en">
<head>
<meta charset="utf-8">
<title>Meadowbrook Pet Hospital – Trifold Brochure</title>
<link href="https://fonts.googleapis.com/css2?family=Lato:ital,wght@0,400;0,700;0,900;1,400&family=Lobster&family=Lobster+Two:wght@700&display=swap" rel="stylesheet">
<style>
:root{
  --canvas:#e9eaec;
  --orange:#ef8a4e;
  --orange-deep:#e0703a;
  --green:#7ea84c;
  --green-soft:#cfdfc3;
  --brown:#5b3b24;
  --brown-text:#4a3324;
  --ink:#3b2e25;
  --cream:#f6f1e6;
}
*{box-sizing:border-box;margin:0;padding:0}
html,body{width:1200px;height:1000px;overflow:hidden}
body{background:var(--canvas);font-family:"Lato",sans-serif;color:var(--ink);position:relative}
.sheet{position:absolute;box-shadow:0 6px 14px rgba(0,0,0,.18)}
.outside{left:280px;top:52px;width:635px;height:448px;display:flex}
.panel{position:relative;height:100%;overflow:hidden}
.about{width:212px;background:linear-gradient(180deg,#c9cfc9 0%,#dcd6c8 45%,#c9a57c 80%,#b88d63 100%)}
.about-photo{position:absolute;inset:0;background:linear-gradient(180deg,rgba(255,255,255,.5) 0%,rgba(235,228,214,.3) 40%,rgba(200,160,110,.25) 100%)}
.about-copy{position:relative;padding:22px 18px 0 20px;font-size:8.6px;line-height:1.2}
.about h2{font-family:"Lobster Two",sans-serif;font-size:16px;color:var(--brown);margin-bottom:4px}
.about p{margin-bottom:9px}
.about ul{list-style:none}
.about li::before{content:"•";color:var(--brown);margin-right:5px}
.circle{position:absolute;border-radius:50%;border:3px solid var(--brown)}
.circle-vet{left:98px;top:172px;width:104px;height:104px;background:radial-gradient(circle at 50% 40%,#b8c7d3,#5f7386)}
.circle-cat{left:10px;top:223px;width:118px;height:118px;background:radial-gradient(circle at 50% 50%,#c8b6a2,#7d6653)}
.hours{width:211px;background:var(--orange);text-align:center;color:var(--brown-text);padding-top:42px}
.hours h3{font-family:"Lobster Two",sans-serif;font-size:13px;margin-bottom:3px}
.hours .times{font-size:9px;line-height:1.25}
.hours .times b{font-weight:900}
.hours .note{font-size:7px;font-style:italic;margin:12px 30px 0;line-height:1.3}
.brand-small{margin-top:50px;font-weight:900;font-size:11px;line-height:1.15;color:var(--brown)}
.brand-small .dot{display:inline-block;width:10px;height:10px;border-radius:50%;background:var(--brown);margin-bottom:4px}
.contact{font-size:8.6px;line-height:1.35;margin-top:14px}
.map{position:absolute;left:13px;top:298px;width:186px;height:140px;border:3px solid var(--brown);padding:4px}
.map div{width:100%;height:100%;background:linear-gradient(135deg,#eef0ea,#dfe5dc);border:1px solid #c9c0b0}
.cover{width:212px;background:linear-gradient(180deg,#c8d3d8 0%,#e4e0d6 40%,#caa982 70%,#6e5440 100%)}
.cover-photo{position:absolute;left:0;right:0;top:230px;bottom:0;background:radial-gradient(ellipse at 70% 40%,#5b4436 0%,#8a6e55 40%,rgba(180,150,110,0) 80%)}
.brand-cover{position:absolute;left:0;right:0;top:64px;text-align:center;font-weight:900;font-size:17px;line-height:1.1;color:var(--brown)}
.brand-cover .dot{display:block;width:16px;height:16px;background:var(--brown);border-radius:50%;margin:0 auto 8px}
.pill{position:absolute;top:402px;height:34px;border-radius:14px;text-align:center;color:var(--brown-text);padding-top:4px;font-weight:900}
.pill small{display:block;font-size:7px}
.pill span{font-size:13px}
.pill-phone{left:11px;width:90px;background:#9bc33c}
.pill-emergency{left:106px;width:96px;background:var(--orange)}

.inside{left:283px;top:520px;width:632px;height:448px;background:var(--green-soft)}
.fold{position:absolute;top:0;bottom:0;width:1px;background:rgba(90,110,80,.15)}
.services-title{position:absolute;left:200px;width:232px;top:38px;text-align:center}
.services-title .brand{font-weight:900;font-size:15px;line-height:1.1;color:var(--brown)}
.services-title .brand .dot{display:block;width:14px;height:14px;border-radius:50%;background:var(--brown);margin:0 auto 6px}
.services-title h1{font-family:"Lobster",sans-serif;font-weight:400;font-size:27px;color:var(--brown);margin-top:8px}
.dash-box{position:absolute;border:1.5px dashed}
.box-puppy{left:8px;top:87px;width:192px;height:90px;border-color:var(--green)}
.box-others{left:429px;top:87px;width:196px;height:90px;border-color:var(--orange-deep)}
.tag{position:absolute;top:-12px;left:50%;transform:translateX(-50%);white-space:nowrap;font-family:"Lobster",sans-serif;font-size:14px;color:#fff;border-radius:12px;padding:2px 16px}
.box-puppy .tag{background:var(--green)}
.box-others .tag{background:var(--orange-deep)}
.box-puppy p{font-size:7.4px;line-height:1.25;color:#6e8a5a;padding:24px 8px 0}
.others-list{display:flex;padding:20px 8px 0;font-family:"Lobster",sans-serif;font-size:8.4px;line-height:1.32;color:var(--orange-deep)}
.others-list ul{list-style:none;flex:1}
.others-list ul+ul{border-left:1px solid var(--orange-deep);padding-left:6px}
.box-care{left:8px;top:198px;width:617px;height:243px;border-color:var(--brown)}
.band{position:absolute;left:107px;top:187px;width:420px;height:24px;background:var(--brown);border-radius:12px;color:#fff;text-align:center;font-family:"Lobster",sans-serif;font-size:14px;padding-top:2px}
.cols{position:absolute;left:8px;top:218px;width:617px;height:222px;display:flex}
.col{flex:1;padding:4px 7px;font-size:7.2px;line-height:1.2;color:var(--ink);overflow:hidden}
.col+.col{border-left:1.5px dashed var(--brown)}
.col h4{font-family:"Lobster Two",sans-serif;font-size:8.6px;color:var(--brown);margin-top:5px}
.col h4:first-child{margin-top:0}
</style>
</head>
<body>

<section class="sheet outside">
  <div class="panel about">
    <div class="about-photo" role="img" aria-label="Soft sky and sandy field photograph with a puppy giving a high five to a hand"></div>
    <div class="about-copy">
      <h2>About Us</h2>
      <p>Meadowbrook Pet Hospital is a <b>Companion Animal Veterinary Hospital in Tamsworth Vale</b> committed to providing excellent care for loved pets and their owners.</p>
      <p style="margin-bottom:2px">To achieve this we:</p>
      <ul>
        <li>Provide a welcoming environment.</li>
        <li>Treat all patients and owners as important.</li>
        <li>Educate owners to help prevent illness.</li>
        <li>When illness occurs, treat with the latest equipment and techniques.</li>
      </ul>
    </div>
    <div class="circle circle-vet" role="img" aria-label="Photo of a vet in surgical cap and mask"></div>
    <div class="circle circle-cat" role="img" aria-label="Photo of a cat being examined"></div>
  </div>

  <div class="panel hours">
    <h3>Regular Opening Hours</h3>
    <div class="times">Appointments are available<br><b>MONDAY - FRIDAY<br>9:00AM-11:00AM | 3:00PM-5:00PM<br>SATURDAY 9:00AM-12:00PM</b></div>
    <p class="note">Appointments in between these times are available on request.<br>We do surgery every weekday between consulting times.</p>
    <div class="brand-small"><span class="dot"></span><br>Meadowbrook Pet Hospital</div>
    <div class="contact">14 Marlow Crescent Tamsworth Vale NSW 2417<br>02 619 38 205<br>www.meadowbrookvets.example</div>
    <div class="map"><div role="img" aria-label="Street map showing the hospital location"></div></div>
  </div>

  <div class="panel cover">
    <div class="cover-photo" role="img" aria-label="Photo of a woman hugging her dog under a cloudy sky"></div>
    <div class="brand-cover"><span class="dot"></span>Meadowbrook<br>Pet Hospital</div>
    <div class="pill pill-phone"><small>Phone</small><span>02 61938205</span></div>
    <div class="pill pill-emergency"><small>After Hours Emergency</small><span>0417 360 592</span></div>
  </div>
</section>

<section class="sheet inside">
  <div class="fold" style="left:211px"></div>
  <div class="fold" style="left:422px"></div>

  <div class="services-title">
    <div class="brand"><span class="dot"></span>Meadowbrook<br>Pet Hospital</div>
    <h1>Our Services</h1>
  </div>

  <div class="dash-box box-puppy">
    <span class="tag">Puppy Pre-School</span>
    <p>Meadowbrook Pet Hospital runs a 5 week puppy class. These are great fun and provide essential socialisation and training for you and your puppy. The classes prevent a range of behavioural issues and are an essential part of our prevention is better than cure philosophy.</p>
  </div>

  <div class="dash-box box-others">
    <span class="tag">Others Services</span>
    <div class="others-list">
      <ul><li>Emergency Surgery,</li><li>Cruciate Repair</li><li>Caesarian</li><li>Orthopaedic Surgery,</li><li>Skin Treatments</li><li>Routine Blood Tests</li></ul>
      <ul><li>Radiology,</li><li>Ultrasound</li><li>Grieving Support</li><li>Aged Care Consults</li><li>Behaviour Consults</li></ul>
    </div>
  </div>

  <div class="dash-box box-care"></div>
  <div class="band">Basic Pet Care</div>
  <div class="cols">
    <div class="col">
      <h4>Yearly Vaccinations &amp; Checkup</h4>
      <p>Essential viral disease prevention. Everyone should vaccinate, but they don't, making vaccinations even more essential because your pets are at risk and we need to establish majority immunity. Please do what's best for pets and the community. We usually do yearly checkup at vaccination. A Vet check is essential at least once per year, twice a year for senior pets.</p>
      <h4>Microchipping</h4>
      <p>Law in NSW. We get strays at the hospital almost everyday. The ones with up to date microchipping details go home with relieved owners. The others go to the pound. Please microchip and keep your details accurate. We see the joy and tears when pets and family's are reunited.</p>
      <h4>Premium Food</h4>
      <p>Your pet will be happier and so will you. A premium food, tailored to your pets breed and age will add 20-30% to the lifespan of your pet. Premium foods reduce smell and volume of faeces, improve dental health, improve coat quality. Premium foods are cost competitive because you don't need to feed as much. The real value is reduced medical, surgical and dental bills.</p>
    </div>
    <div class="col">
      <h4>Heartworming</h4>
      <p>A ghastly parasite that lives in the heart of animals. A yearly Heartworm injection is now available and most people book in yearly for heartworm, vaccination and a checkup. We send reminders for these after you get the first treatment.</p>
      <h4 style="margin-top:14px">Socialisation</h4>
      <p>Mostly applies to happy dogs. Dogs are social animals and thrive on interaction with people and other dogs. Particularly important in puppies to prevent anxiety and aggression. Take your dogs for heaps of walks.</p>
      <h4 style="margin-top:22px">Intestinal worming</h4>
      <p>Done every 3 months to prevent hookworm, whipworm, tapeworm and roundworm. We strongly recommend a vet only brand as we know they contain treatment for all the worms. These treatments only cost a couple of dollars, so you save nothing by risking a supermarket brand. Worming is by weight, so if you can, bring your pet for a weigh in. Also a good chance to get some socialisation and make trips to the vet pleasant.</p>
    </div>
    <div class="col">
      <h4>Sterilisation</h4>
      <p>Dogs and Cats do not understand contraception. If you do not plan to breed, please desex. PLUS, your pet is more prone to diseases such as Ovarian and Testicular Cancer if not desexed. We recommend desexing Kittens over 1kg (About 16 weeks) and puppies 12 weeks. Desexing young has less bleeding, smaller wounds and reduces juvenile and adult behavioural problems.</p>
      <h4>Flea Treatment</h4>
      <p>Monthly prevention all year round please. Even in winter, keep up the prevention. Check out the flea life cycle and you will see why. And remember to do all animals, including the cats. Cats hide fleas better than dogs, but they continue the lifecycle.</p>
      <h4>Dental Care</h4>
      <p>Good teeth means a good diet and a healthy pet. These are a free service run by our awesome nurses. Book in any time and we will have a look.</p>
      <h4>Environmental Enrichment</h4>
      <p>Fun is good. Keep your pets busy and they will have less anxiety and destruction.</p>
    </div>
  </div>
</section>

</body>
</html>
```